Cybersecurity Start-Up - Tervalo

We need a power-point design for a new company based in Madrid (Spain) called 'Tervalo'. We aim to provide cybersecurity services to small- medium size companies for whom security is critical but paying big money to huge companies is not affordable.

The final design should communicate several things. As technology company which provides cybersecurity, it should be seen as something modern and futuristic , combined with safety and protection.

The company name Tervalo comes from Tervalosa, an ancient Celtiberian settlement in Spain which is famous for its role in the Celtiberian Wars (130 BC). They fought with Rome for 20 years , while being numerical inferior. And they won several times. When a final siege ocurred after a massive deployment of Rome legions, they held their ground for more than a year without food. When the situation was not longer sustainable, they decided to commit suicide rather than become slaves.

So the vision to hold the ground no matter what, should be communicated too
Updates

Need extra days to review

Requirements
Must have
• Check files attached for the logo of the company

```html
<!DOCTYPE html>
<html lang="en">
<head>
<meta charset="utf-8">
<title>Tervalo – Presentation Template</title>
<link href="https://fonts.googleapis.com/css2?family=Roboto+Condensed:wght@400;700&family=Open+Sans:wght@400;600;700&display=swap" rel="stylesheet">
<style>
:root{
  --page:#e4e5e6;
  --navy:#0f1e33;
  --navy-2:#16304f;
  --steel:#2b4a6e;
  --orange:#f15a22;
  --grey:#8d9094;
  --grey-light:#c9cbce;
  --ink:#3a3d42;
  --white:#ffffff;
}
*{box-sizing:border-box;margin:0;padding:0}
html,body{width:1200px;height:900px;overflow:hidden;background:var(--page);font-family:"Open Sans",sans-serif}
.deck{position:absolute;left:170px;top:76px;display:grid;grid-template-columns:repeat(3,261px);grid-auto-rows:147px;gap:3px}
.slide{position:relative;overflow:hidden;background:var(--white)}
.slide--dark{background:var(--navy)}
.abs{position:absolute}
.photo{position:absolute}
.head{font-family:"Roboto Condensed",sans-serif;color:var(--white);text-transform:uppercase}

/* header bar */
.bar{position:absolute;left:0;top:0;width:100%;height:14px;background:linear-gradient(90deg,var(--navy) 0%,var(--navy-2) 55%,var(--navy) 100%)}
.bar__title{position:absolute;left:11px;top:3px;font-family:"Roboto Condensed",sans-serif;font-size:7px;color:var(--white)}
.bar__stripe{position:absolute;right:0;top:9px;width:85px;height:5px}
/* footer */
.foot{position:absolute;left:11px;right:11px;bottom:9px;border-top:.5px solid #d6d7d9}
.foot__num{position:absolute;left:0;top:1px;font-size:2.6px;color:var(--grey)}
.foot__brand{position:absolute;right:0;top:.5px;font-size:3.2px;font-weight:700;color:var(--navy)}

.tiny{font-size:3.1px;line-height:4.3px;color:var(--ink);text-align:justify}
.tiny--c{text-align:center}
.tiny--w{color:var(--white)}
.label{font-size:3.4px;line-height:4.4px;font-weight:700;color:var(--orange)}
.title-o{font-size:5.6px;color:var(--orange);font-weight:600}
.brand{font-family:"Open Sans",sans-serif;font-weight:700;color:var(--white)}
</style>
</head>
<body>
<main class="deck">

  <!-- 1 Cover -->
  <section class="slide slide--dark">
    <svg class="abs" width="261" height="147" viewBox="0 0 261 147" role="img" aria-label="Photo of a hand touching a glowing hexagon security interface">
      <defs>
        <linearGradient id="coverPhoto" x1="0" y1="0" x2="1" y2="1">
          <stop offset="0" stop-color="#2c4a70"/><stop offset=".5" stop-color="#6f8aa8"/><stop offset="1" stop-color="#1b3456"/>
        </linearGradient>
      </defs>
      <path d="M104 0 C118 70 150 120 200 147 L261 147 L261 0 Z" fill="url(#coverPhoto)"/>
      <path d="M104 0 C118 70 150 120 200 147" fill="none" stroke="var(--orange)" stroke-width="4"/>
      <path d="M252 70 C250 105 238 130 222 147" fill="none" stroke="var(--orange)" stroke-width="3"/>
    </svg>
    <div class="abs brand" style="left:12px;top:11px;font-size:9px">Tervalo</div>
    <div class="abs head" style="left:25px;top:91px;font-size:15px">Welcome</div>
    <div class="abs head" style="left:25px;top:108px;font-size:6px;letter-spacing:1.2px">To our presentation</div>
    <div class="abs" style="left:25px;top:117px;font-size:3.6px;color:var(--orange);font-weight:600">Madrid, March 25, 2018</div>
  </section>

  <!-- 2 Table of contents -->
  <section class="slide slide--dark">
    <div class="photo" style="inset:0;background:radial-gradient(circle at 45% 45%,#2f5f7c 0%,#1a3650 45%,#0d1c2e 100%)" role="img" aria-label="Padlock over a digital binary background"></div>
    <div class="abs head" style="left:40px;top:39px;font-size:3.6px">Table of</div>
    <div class="abs head" style="left:40px;top:44px;font-size:9px">Contents</div>
    <div class="abs" style="left:56px;top:75px;width:180px;display:grid;grid-template-columns:1fr 1fr;row-gap:9px">
      <div style="display:flex;gap:4px;align-items:center"><span style="width:9px;height:9px;border-radius:50%;background:var(--orange);border:1px solid #fff;color:#fff;font-size:4px;display:grid;place-items:center">1</span><span class="head" style="font-size:3.2px;line-height:4px">Lorem ipsum dolor sit<br>met dolor sit met</span></div>
      <div style="display:flex;gap:4px;align-items:center"><span style="width:9px;height:9px;border-radius:50%;background:var(--orange);border:1px solid #fff;color:#fff;font-size:4px;display:grid;place-items:center">4</span><span class="head" style="font-size:3.2px;line-height:4px">Lorem ipsum dolor sit<br>met dolor sit met</span></div>
      <div style="display:flex;gap:4px;align-items:center"><span style="width:9px;height:9px;border-radius:50%;background:var(--orange);border:1px solid #fff;color:#fff;font-size:4px;display:grid;place-items:center">2</span><span class="head" style="font-size:3.2px;line-height:4px">Lorem ipsum dolor sit<br>met dolor sit met</span></div>
      <div style="display:flex;gap:4px;align-items:center"><span style="width:9px;height:9px;border-radius:50%;background:var(--orange);border:1px solid #fff;color:#fff;font-size:4px;display:grid;place-items:center">5</span><span class="head" style="font-size:3.2px;line-height:4px">Lorem ipsum dolor sit<br>met dolor sit met</span></div>
      <div style="display:flex;gap:4px;align-items:center"><span style="width:9px;height:9px;border-radius:50%;background:var(--orange);border:1px solid #fff;color:#fff;font-size:4px;display:grid;place-items:center">3</span><span class="head" style="font-size:3.2px;line-height:4px">Lorem ipsum dolor sit<br>met dolor sit met</span></div>
      <div style="display:flex;gap:4px;align-items:center"><span style="width:9px;height:9px;border-radius:50%;background:var(--orange);border:1px solid #fff;color:#fff;font-size:4px;display:grid;place-items:center">6</span><span class="head" style="font-size:3.2px;line-height:4px">Lorem ipsum dolor sit<br>met dolor sit met</span></div>
    </div>
  </section>

  <!-- 3 About us: banner -->
  <section class="slide">
    <div class="bar"><span class="bar__title">About us</span><svg class="bar__stripe" viewBox="0 0 85 5"><polygon points="8,0 85,0 85,5 0,5" fill="var(--orange)"/></svg></div>
    <div class="abs" style="left:0;top:35px;width:84px;height:47px;background:var(--orange);padding:13px 16px 0">
      <p class="head" style="font-size:2.9px;line-height:4px;font-weight:700">Lorem ipsum dolor sit met consectur adipiscing elit sed do eiusmod tempor incididunt ut labore et dolore magna</p>
    </div>
    <div class="photo" style="left:84px;top:35px;width:177px;height:47px;background:linear-gradient(90deg,#1e4f86,#5b8fc4 60%,#a8c6e2)" role="img" aria-label="Business person touching a digital data interface"></div>
    <p class="abs tiny" style="left:84px;top:90px;width:166px">Lorem ipsum dolor sit amet, consectetur adipiscing elit, sed do eiusmod tempor incididunt ut labore et dolore magna aliqua. Ut enim ad minim veniam, quis nostrud exercitation ullamco laboris nisi ut aliquip ex ea commodo consequat. Duis aute irure dolor in reprehenderit in voluptate velit esse cillum dolore eu fugiat nulla pariatur.</p>
    <div class="foot"><span class="foot__num">02</span><span class="foot__brand">Tervalo</span></div>
  </section>

  <!-- 4 About us: columns -->
  <section class="slide">
    <div class="bar"><span class="bar__title">About us</span><svg class="bar__stripe" viewBox="0 0 85 5"><polygon points="8,0 85,0 85,5 0,5" fill="var(--orange)"/></svg></div>
    <div class="photo" style="left:11px;top:37px;width:56px;height:34px;background:linear-gradient(135deg,#0e2a47,#2f6a9a 60%,#0e2a47)" role="img" aria-label="Finger touching a glowing padlock screen"></div>
    <p class="abs label" style="left:11px;top:74px;width:56px;text-align:right;font-weight:600">Lorem ipsum dolor sit amet consectetur adipiscing et sed do eiusmod</p>
    <div class="abs" style="left:76px;top:37px;width:80px">
      <p class="tiny">Lorem ipsum dolor sit amet, consectetur adipiscing elit, sed do eiusmod tempor incididunt ut labore et dolore magna aliqua. Ut enim ad minim veniam, quis nostrud exercitation ullamco laboris nisi ut aliquip ex ea commodo consequat. Duis aute irure dolor in reprehenderit in voluptate velit esse cillum dolore eu fugiat nulla pariatur.</p>
      <p class="tiny" style="margin-top:3px">Lorem ipsum dolor sit amet, consectetur adipiscing elit, sed do eiusmod tempor incididunt ut labore et dolore magna aliqua. Ut enim ad minim veniam, quis nostrud exercitation ullamco laboris nisi ut aliquip ex ea commodo.</p>
    </div>
    <div class="abs" style="left:167px;top:37px;width:80px">
      <p class="tiny">Lorem ipsum dolor sit amet, consectetur adipiscing elit, sed do eiusmod tempor incididunt ut labore et dolore magna aliqua. Ut enim ad minim veniam, quis nostrud exercitation ullamco laboris nisi ut aliquip ex ea commodo consequat. Duis aute irure dolor in reprehenderit in voluptate velit esse cillum dolore eu fugiat nulla pariatur.</p>
      <p class="tiny" style="margin-top:3px">Lorem ipsum dolor sit amet, consectetur adipiscing elit, sed do eiusmod tempor incididunt ut labore et dolore magna aliqua. Ut enim ad minim veniam, quis nostrud exercitation ullamco laboris nisi ut aliquip ex ea commodo.</p>
    </div>
    <div class="foot"><span class="foot__num">02</span><span class="foot__brand">Tervalo</span></div>
  </section>

  <!-- 5 About us: three images -->
  <section class="slide">
    <div class="bar"><span class="bar__title">About us</span><svg class="bar__stripe" viewBox="0 0 85 5"><polygon points="8,0 85,0 85,5 0,5" fill="var(--orange)"/></svg></div>
    <p class="abs title-o" style="left:15px;top:35px">Lorem ipsum dolor sit amet</p>
    <div class="abs" style="left:15px;top:46px;width:90px">
      <p class="tiny">Lorem ipsum dolor sit amet, consectetur adipiscing elit, sed do eiusmod tempor incididunt ut labore et dolore magna aliqua. Ut enim ad minim veniam, quis nostrud exercitation ullamco laboris nisi ut aliquip ex ea commodo consequat. Duis aute irure dolor in reprehenderit in voluptate velit esse cillum dolore eu fugiat nulla pariatur.</p>
      <p class="tiny" style="margin-top:4px">Lorem ipsum dolor sit amet, consectetur adipiscing elit, sed do eiusmod tempor incididunt ut labore et dolore magna aliqua. Ut enim ad minim veniam, quis.</p>
    </div>
    <div class="photo" style="left:115px;top:32px;width:37px;height:44px;background:linear-gradient(135deg,#0f1e33,#a24a22 70%,#e58a3c)" role="img" aria-label="Hand touching a glowing digital lock"></div>
    <div class="photo" style="left:162px;top:32px;width:37px;height:44px;background:linear-gradient(135deg,#3c7fc0,#9cc7ea 60%,#2a5f96)" role="img" aria-label="Person working on a tablet with data overlay"></div>
    <div class="photo" style="left:208px;top:32px;width:37px;height:44px;background:linear-gradient(135deg,#0d2a52,#3f83c9 60%,#0d2a52)" role="img" aria-label="Hand holding a glowing globe network"></div>
    <p class="abs tiny" style="left:115px;top:81px;width:37px">Duis aute irure dolor in reprehenderit in voluptate velit esse cillum dolore eu fugiat nulla pariatur.</p>
    <p class="abs tiny" style="left:162px;top:81px;width:37px">Duis aute irure dolor in reprehenderit in voluptate velit esse cillum dolore eu fugiat nulla pariatur.</p>
    <p class="abs tiny" style="left:208px;top:81px;width:37px">Duis aute irure dolor in reprehenderit in voluptate velit esse cillum dolore eu fugiat nulla pariatur.</p>
    <div class="foot"><span class="foot__num">02</span><span class="foot__brand">Tervalo</span></div>
  </section>

  <!-- 6 About us: icons -->
  <section class="slide">
    <div class="photo" style="left:0;top:0;width:261px;height:84px;background:linear-gradient(180deg,#2c3f5a,#6c7f96 55%,#3a4c64)" role="img" aria-label="Hooded figure working on a laptop"></div>
    <div class="bar"><span class="bar__title">About us</span><svg class="bar__stripe" viewBox="0 0 85 5"><polygon points="8,0 85,0 85,5 0,5" fill="var(--orange)"/></svg></div>
    <svg class="abs" style="left:0;top:84px" width="261" height="60" viewBox="0 0 261 60">
      <g fill="#fff" stroke="var(--orange)" stroke-width="1.2">
        <circle cx="41" cy="12" r="8"/><circle cx="102" cy="12" r="8"/><circle cx="165" cy="12" r="8"/><circle cx="222" cy="12" r="8"/>
      </g>
      <g fill="none" stroke="var(--orange)" stroke-width="1">
        <circle cx="40" cy="11" r="3"/><line x1="42" y1="13" x2="44.5" y2="15.5"/>
        <circle cx="165" cy="12.5" r="3.2"/><line x1="165" y1="12.5" x2="165" y2="10.5"/><line x1="164" y1="8" x2="166" y2="8"/>
      </g>
      <g fill="var(--orange)">
        <rect x="99" y="13" width="1.6" height="3"/><rect x="101.5" y="11" width="1.6" height="5"/><rect x="104" y="9" width="1.6" height="7"/>
        <path d="M224 8 L219 12 L224 16 L222 12 Z"/>
      </g>
    </svg>
    <p class="abs tiny tiny--c" style="left:20px;top:105px;width:42px;font-weight:600">Dolor sit amet, consectetur adipiscing elit, sed do eiusmod tempor</p>
    <p class="abs tiny tiny--c" style="left:81px;top:105px;width:42px;font-weight:600">Dolor sit amet, consectetur adipiscing elit, sed do eiusmod tempor</p>
    <p class="abs tiny tiny--c" style="left:144px;top:105px;width:42px;font-weight:600">Dolor sit amet, consectetur adipiscing elit, sed do eiusmod tempor</p>
    <p class="abs tiny tiny--c" style="left:201px;top:105px;width:42px;font-weight:600">Dolor sit amet, consectetur adipiscing elit, sed do eiusmod tempor</p>
    <div class="foot"><span class="foot__num">02</span><span class="foot__brand">Tervalo</span></div>
  </section>

  <!-- 7 About us: cycle diagram -->
  <section class="slide">
    <div class="bar"><span class="bar__title">About us</span><svg class="bar__stripe" viewBox="0 0 85 5"><polygon points="8,0 85,0 85,5 0,5" fill="var(--orange)"/></svg></div>
    <svg class="abs" style="left:93px;top:40px" width="80" height="80" viewBox="0 0 80 80">
      <g fill="none" stroke-width="22">
        <circle cx="40" cy="40" r="28" stroke="var(--orange)" stroke-dasharray="40 136" transform="rotate(182 40 40)"/>
        <circle cx="40" cy="40" r="28" stroke="var(--grey-light)" stroke-dasharray="40 136" transform="rotate(272 40 40)"/>
        <circle cx="40" cy="40" r="28" stroke="var(--navy)" stroke-dasharray="40 136" transform="rotate(2 40 40)"/>
        <circle cx="40" cy="40" r="28" stroke="var(--grey)" stroke-dasharray="40 136" transform="rotate(92 40 40)"/>
      </g>
      <g fill="none" stroke="#fff" stroke-width=".8">
        <circle cx="40" cy="12" r="6"/><circle cx="68" cy="40" r="6"/><circle cx="40" cy="68" r="6"/><circle cx="12" cy="40" r="6"/>
      </g>
      <path d="M37 14 L44 9 L41 15 Z" fill="#fff"/>
      <path d="M40 65 a2.5 2.5 0 1 1 0.1 0 M40 71 l-2 -4 h4 z" fill="#fff"/>
      <path d="M9 38 h6 l-3 4 z" fill="none" stroke="#fff" stroke-width=".6"/>
      <circle cx="68" cy="40" r="2.5" fill="none" stroke="#fff" stroke-width=".6"/>
    </svg>
    <svg class="abs" style="left:30px;top:42px" width="8" height="8" viewBox="0 0 8 8"><path d="M1 4 L7 1 L5 7 L4 4.5 Z" fill="none" stroke="var(--orange)" stroke-width=".6"/></svg>
    <p class="abs" style="left:40px;top:42px;font-size:5.4px;color:var(--orange)">Lorem ipsum</p>
    <p class="abs tiny" style="left:27px;top:51px;width:45px;text-align:right">Dolor sit amet, consectetur adipiscing elit, sed do eiusmod tempor</p>
    <p class="abs" style="left:40px;top:84px;font-size:5.4px;color:var(--grey)">Lorem ipsum</p>
    <p class="abs tiny" style="left:27px;top:93px;width:45px;text-align:right">Dolor sit amet, consectetur adipiscing elit, sed do eiusmod tempor</p>
    <p class="abs" style="left:191px;top:42px;font-size:5.4px;color:var(--grey)">Lorem ipsum</p>
    <p class="abs tiny" style="left:182px;top:51px;width:45px;text-align:left">Dolor sit amet, consectetur adipiscing elit, sed do eiusmod tempor</p>
    <p class="abs" style="left:191px;top:84px;font-size:5.4px;color:var(--navy)">Lorem ipsum</p>
    <p class="abs tiny" style="left:182px;top:93px;width:45px;text-align:left">Dolor sit amet, consectetur adipiscing elit, sed do eiusmod tempor</p>
    <div class="foot"><span class="foot__num">02</span><span class="foot__brand">Tervalo</span></div>
  </section>

  <!-- 8 About us: donut chart -->
  <section class="slide">
    <div class="bar"><span class="bar__title">About us</span><svg class="bar__stripe" viewBox="0 0 85 5"><polygon points="8,0 85,0 85,5 0,5" fill="var(--orange)"/></svg></div>
    <svg class="abs" style="left:0;top:0" width="261" height="147" viewBox="0 0 261 147">
      <g fill="none" stroke-width="13" transform="rotate(-90 86 79)">
        <circle cx="86" cy="79" r="30" stroke="var(--orange)" stroke-dasharray="109.3 188.5"/>
        <circle cx="86" cy="79" r="30" stroke="var(--grey-light)" stroke-dasharray="22.6 188.5" stroke-dashoffset="-109.3"/>
        <circle cx="86" cy="79" r="30" stroke="var(--grey)" stroke-dasharray="24.5 188.5" stroke-dashoffset="-131.9"/>
        <circle cx="86" cy="79" r="30" stroke="var(--navy)" stroke-dasharray="32 188.5" stroke-dashoffset="-156.4"/>
      </g>
      <circle cx="86" cy="79" r="18" fill="var(--orange)"/>
      <g fill="var(--navy)"><circle cx="86" cy="68" r="2.5"/><rect x="83" y="71.5" width="6" height="9" rx="1"/><rect x="83.6" y="80" width="2.2" height="8"/><rect x="86.2" y="80" width="2.2" height="8"/></g>
      <g stroke="var(--navy)" stroke-width=".5" fill="none">
        <polyline points="38,45 38,50 70,50"/><polyline points="110,52 110,45 160,45"/><polyline points="34,96 34,100 60,100"/><polyline points="22,47 22,57"/>
      </g>
    </svg>
    <p class="abs" style="left:25px;top:38px;font-size:7px;font-weight:700;color:var(--navy)">17%</p>
    <p class="abs" style="left:18px;top:57px;font-size:7px;font-weight:700;color:var(--grey)">13%</p>
    <p class="abs" style="left:30px;top:110px;font-size:7px;font-weight:700;color:var(--navy)">12%</p>
    <p class="abs" style="left:130px;top:33px;font-size:11px;font-weight:700;color:var(--orange)">58%</p>
    <p class="abs" style="left:160px;top:64px;font-size:3.4px;font-weight:700;color:var(--navy)">Lorem ipsum dolor sit amet,</p>
    <p class="abs tiny" style="left:160px;top:70px;width:82px">consectetur adipiscing elit, sed do eiusmod tempor incididunt ut labore et dolore magna aliqua. Ut enim ad minim veniam, quis nostrud exercitation ullamco laboris nisi ut aliquip ex ea commodo consequat. Duis aute irure dolor in reprehenderit in voluptate velit esse cillum</p>
    <div class="foot"><span class="foot__num">02</span><span class="foot__brand">Tervalo</span></div>
  </section>

  <!-- 9 About us: icon panel -->
  <section class="slide">
    <div class="bar"><span class="bar__title">About us</span><svg class="bar__stripe" viewBox="0 0 85 5"><polygon points="8,0 85,0 85,5 0,5" fill="var(--orange)"/></svg></div>
    <div class="photo" style="left:19px;top:22px;width:80px;height:109px;background:linear-gradient(160deg,#1c3552,#0f1e33)" role="img" aria-label="Dark digital code background"></div>
    <svg class="abs" style="left:19px;top:22px" width="80" height="109" viewBox="0 0 80 109">
      <g stroke="#fff" stroke-width=".4"><line x1="40" y1="26" x2="40" y2="88"/><line x1="8" y1="57" x2="72" y2="57"/></g>
      <g fill="var(--orange)"><path d="M24 28 l-4 4 l4 4 l-1.5 -4 z"/><rect x="20" y="60" width="1.5" height="3"/><rect x="22.5" y="58" width="1.5" height="5"/><rect x="25" y="56" width="1.5" height="7"/></g>
      <g fill="none" stroke="var(--orange)" stroke-width=".8"><circle cx="58" cy="31" r="2.5"/><line x1="60" y1="33" x2="62" y2="35"/><circle cx="57" cy="60" r="2.8"/></g>
    </svg>
    <p class="abs tiny tiny--w tiny--c" style="left:28px;top:62px;width:30px;font-size:2.5px;line-height:3.3px">Dolor sit amet, consectetur adipiscing elit, sed do eiusmod tempor</p>
    <p class="abs tiny tiny--w tiny--c" style="left:62px;top:62px;width:30px;font-size:2.5px;line-height:3.3px">Dolor sit amet, consectetur adipiscing elit, sed do eiusmod tempor</p>
    <p class="abs tiny tiny--w tiny--c" style="left:28px;top:92px;width:30px;font-size:2.5px;line-height:3.3px">Dolor sit amet, consectetur adipiscing elit, sed do eiusmod tempor</p>
    <p class="abs tiny tiny--w tiny--c" style="left:62px;top:92px;width:30px;font-size:2.5px;line-height:3.3px">Dolor sit amet, consectetur adipiscing elit, sed do eiusmod tempor</p>
    <p class="abs title-o" style="left:122px;top:44px">Lorem ipsum dolor sit amet</p>
    <div class="abs" style="left:122px;top:54px;width:104px">
      <p class="tiny">Lorem ipsum dolor sit amet, consectetur adipiscing elit, sed do eiusmod tempor incididunt ut labore et dolore magna aliqua. Ut enim ad minim veniam, quis nostrud exercitation ullamco laboris nisi ut aliquip ex ea commodo consequat. Duis aute irure dolor in reprehenderit in voluptate velit esse cillum dolore eu fugiat nulla pariatur.</p>
      <p class="tiny" style="margin-top:4px">Lorem ipsum dolor sit amet, consectetur adipiscing elit, sed do eiusmod tempor incididunt ut labore et dolore magna aliqua. Ut enim ad minim veniam, quis nostrud exercitation ullamco laboris nisi ut aliquip ex ea commodo consequat.</p>
    </div>
    <div class="foot"><span class="foot__num">02</span><span class="foot__brand">Tervalo</span></div>
  </section>

  <!-- 10 About us: bar chart -->
  <section class="slide">
    <div class="bar"><span class="bar__title">About us</span><svg class="bar__stripe" viewBox="0 0 85 5"><polygon points="8,0 85,0 85,5 0,5" fill="var(--orange)"/></svg></div>
    <div class="abs" style="left:24px;top:45px;width:120px">
      <p class="label">Lorem ipsum dolor sit amet</p>
      <p class="tiny">consectetur adipiscing elit, sed do eiusmod tempor incididunt ut labore et dolore magna aliqua. Ut enim ad minim veniam, quis nostrud exercitation ullamco laboris nisi ut aliquip ex ea commodo consequat. Duis aute irure dolor in reprehenderit in voluptate velit esse cillum dolore eu fugiat nulla pariatur.</p>
      <p class="label" style="margin-top:4px">Lorem ipsum dolor sit amet</p>
      <p class="tiny">consectetur adipiscing elit, sed do eiusmod tempor incididunt ut labore et dolore magna aliqua. Ut enim ad minim veniam, quis nostrud exercitation ullamco laboris nisi ut aliquip ex ea commodo consequat. Duis aute irure dolor in reprehenderit in voluptate velit esse cillum dolore eu.</p>
    </div>
    <svg class="abs" style="left:166px;top:26px" width="84" height="54" viewBox="0 0 84 54" role="img" aria-label="Bar chart 2009 to 2012">
      <line x1="4" y1="48" x2="80" y2="48" stroke="var(--grey-light)" stroke-width=".5"/>
      <g>
        <rect x="6" y="14" width="3" height="34" fill="var(--navy)"/><rect x="10" y="30" width="3" height="18" fill="var(--grey-light)"/><rect x="14" y="22" width="3" height="26" fill="var(--orange)"/>
        <rect x="25" y="26" width="3" height="22" fill="var(--navy)"/><rect x="29" y="18" width="3" height="30" fill="var(--grey-light)"/><rect x="33" y="28" width="3" height="20" fill="var(--orange)"/>
        <rect x="44" y="16" width="3" height="32" fill="var(--navy)"/><rect x="48" y="20" width="3" height="28" fill="var(--grey-light)"/><rect x="52" y="24" width="3" height="24" fill="var(--orange)"/>
        <rect x="63" y="20" width="3" height="28" fill="var(--navy)"/><rect x="67" y="26" width="3" height="22" fill="var(--grey-light)"/><rect x="71" y="8" width="3" height="40" fill="var(--orange)"/>
      </g>
      <g font-size="2.6" fill="var(--ink)" font-family="Open Sans,sans-serif"><text x="7" y="53">2009</text><text x="26" y="53">2010</text><text x="45" y="53">2011</text><text x="64" y="53">2012</text></g>
    </svg>
    <div class="abs" style="left:176px;top:84px;width:60px">
      <p class="tiny" style="font-size:2.6px;line-height:3.3px"><span style="display:inline-block;width:2.5px;height:2.5px;background:var(--navy);margin-right:3px"></span><b>LOREM IPSUM</b><br>&nbsp;&nbsp;&nbsp;Lorem ipsum dolor sit amet consectetur</p>
      <p class="tiny" style="font-size:2.6px;line-height:3.3px;margin-top:4px"><span style="display:inline-block;width:2.5px;height:2.5px;background:var(--grey-light);margin-right:3px"></span><b>LOREM IPSUM</b><br>&nbsp;&nbsp;&nbsp;Lorem ipsum dolor sit amet consectetur</p>
      <p class="tiny" style="font-size:2.6px;line-height:3.3px;margin-top:4px"><span style="display:inline-block;width:2.5px;height:2.5px;background:var(--orange);margin-right:3px"></span><b>LOREM IPSUM</b></p>
    </div>
    <div class="foot"><span class="foot__num">02</span><span class="foot__brand">Tervalo</span></div>
  </section>

  <!-- 11 About us: progress rings -->
  <section class="slide">
    <div class="bar"><span class="bar__title">About us</span><svg class="bar__stripe" viewBox="0 0 85 5"><polygon points="8,0 85,0 85,5 0,5" fill="var(--orange)"/></svg></div>
    <svg class="abs" style="left:0;top:0" width="261" height="147" viewBox="0 0 261 147">
      <g fill="none" stroke-width="3">
        <circle cx="58" cy="64" r="15" stroke="var(--navy)"/><circle cx="58" cy="64" r="15" stroke="var(--orange)" stroke-dasharray="76.3 94.2" transform="rotate(-90 58 64)"/>
        <circle cx="134" cy="64" r="15" stroke="var(--grey-light)"/><circle cx="134" cy="64" r="15" stroke="var(--orange)" stroke-dasharray="67.8 94.2" transform="rotate(-90 134 64)"/>
        <circle cx="208" cy="64" r="15" stroke="var(--navy)"/><circle cx="208" cy="64" r="15" stroke="var(--orange)" stroke-dasharray="59.3 94.2" transform="rotate(-90 208 64)"/>
      </g>
      <g font-family="Roboto Condensed,sans-serif" font-size="6" font-weight="700" fill="var(--orange)" text-anchor="middle">
        <text x="58" y="66">81%</text><text x="134" y="66">72%</text><text x="208" y="66">63%</text>
      </g>
    </svg>
    <p class="abs tiny tiny--c" style="left:32px;top:85px;width:52px">dolor sit amet, consectetur adipiscing elit, sed do eiusmod tempor incididunt ut labore et dolore magna aliqua. Ut enim ad minim veniam, quis nostrud exercitation ullamco laboris nisi ut aliquip ex ea commodo consequat fugiat nulla pariatur.</p>
    <p class="abs tiny tiny--c" style="left:108px;top:85px;width:52px">dolor sit amet, consectetur adipiscing elit, sed do eiusmod tempor incididunt ut labore et dolore magna aliqua. Ut enim ad minim veniam, quis nostrud exercitation ullamco laboris nisi ut aliquip ex ea commodo consequat fugiat nulla pariatur.</p>
    <p class="abs tiny tiny--c" style="left:182px;top:85px;width:52px">dolor sit amet, consectetur adipiscing elit, sed do eiusmod tempor incididunt ut labore et dolore magna aliqua. Ut enim ad minim veniam, quis nostrud exercitation ullamco laboris nisi ut aliquip ex ea commodo consequat fugiat nulla pariatur.</p>
    <div class="foot"><span class="foot__num">02</span><span class="foot__brand">Tervalo</span></div>
  </section>

  <!-- 12 About us: team -->
  <section class="slide">
    <div class="bar"><span class="bar__title">About us</span><svg class="bar__stripe" viewBox="0 0 85 5"><polygon points="8,0 85,0 85,5 0,5" fill="var(--orange)"/></svg></div>
    <svg class="abs" style="left:0;top:0" width="261" height="147" viewBox="0 0 261 147">
      <g stroke="var(--orange)" stroke-width="1.2">
        <circle cx="50" cy="58" r="15" fill="#c8ccd2" role="img" aria-label="Portrait of Jonathan Doe"/>
        <circle cx="129" cy="58" r="15" fill="#d2b9a8" role="img" aria-label="Portrait of Melanie Doe"/>
        <circle cx="210" cy="58" r="15" fill="#cfd1d4" role="img" aria-label="Portrait of Natalie Doe"/>
      </g>
    </svg>
    <p class="abs tiny tiny--c" style="left:25px;top:77px;width:50px;font-weight:700;color:var(--navy)">JONATHAN DOE</p>
    <p class="abs tiny tiny--c" style="left:25px;top:81px;width:50px;font-size:2.5px">President</p>
    <p class="abs tiny tiny--c" style="left:104px;top:77px;width:50px;font-weight:700;color:var(--navy)">MELANIE DOE</p>
    <p class="abs tiny tiny--c" style="left:104px;top:81px;width:50px;font-size:2.5px">CEO / Founder</p>
    <p class="abs tiny tiny--c" style="left:185px;top:77px;width:50px;font-weight:700;color:var(--navy)">NATALIE DOE</p>
    <p class="abs tiny tiny--c" style="left:185px;top:81px;width:50px;font-size:2.5px">Vice President</p>
    <p class="abs tiny tiny--c" style="left:27px;top:89px;width:46px">dolor sit amet, consectetur adipiscing elit, sed do eiusmod tempor incididunt ut labore et dolore magna aliqua. Ut enim ad minim veniam, quis nostrud exercitation.</p>
    <p class="abs tiny tiny--c" style="left:106px;top:89px;width:46px">dolor sit amet, consectetur adipiscing elit, sed do eiusmod tempor incididunt ut labore et dolore magna aliqua. Ut enim ad minim veniam, quis nostrud exercitation.</p>
    <p class="abs tiny tiny--c" style="left:187px;top:89px;width:46px">dolor sit amet, consectetur adipiscing elit, sed do eiusmod tempor incididunt ut labore et dolore magna aliqua. Ut enim ad minim veniam, quis nostrud exercitation.</p>
    <div class="foot"><span class="foot__num">02</span><span class="foot__brand">Tervalo</span></div>
  </section>

  <!-- 13 About us: orange panel -->
  <section class="slide slide--dark">
    <div class="photo" style="left:112px;top:0;width:149px;height:147px;background:radial-gradient(circle at 55% 40%,#7fc3f2 0%,#2c6aa8 30%,#13304f 70%,#0f1e33 100%)" role="img" aria-label="Open hand holding a glowing digital globe"></div>
    <div class="abs" style="left:0;top:0;width:112px;height:147px;background:var(--orange)"></div>
    <p class="abs head" style="left:9px;top:9px;font-size:7px;text-transform:uppercase">About us</p>
    <div class="abs" style="left:9px;top:17px;width:14px;height:.5px;background:#fff"></div>
    <div class="abs" style="left:13px;top:38px;width:90px">
      <p class="tiny tiny--w" style="font-weight:600">Lorem ipsum dolor sit amet</p>
      <p class="tiny tiny--w" style="font-weight:600">consectetur adipiscing elit, sed do eiusmod tempor incididunt ut labore et dolore magna aliqua. Ut enim ad minim veniam, quis nostrud exercitation ullamco laboris nisi ut aliquip ex ea commodo consequat. Duis aute irure dolor in reprehenderit in voluptate velit esse cillum dolore eu fugiat nulla pariatur.</p>
      <p class="tiny tiny--w" style="font-weight:600;margin-top:4px">Lorem ipsum dolor sit amet</p>
      <p class="tiny tiny--w" style="font-weight:600">consectetur adipiscing elit, sed do eiusmod tempor incididunt ut labore et dolore magna aliqua. Ut enim ad minim veniam, quis nostrud exercitation ullamco laboris nisi ut aliquip ex ea commodo consequat.</p>
    </div>
    <p class="abs brand" style="left:5px;top:137px;font-size:4px">Tervalo</p>
  </section>

  <!-- 14 Section title -->
  <section class="slide slide--dark">
    <div class="photo" style="inset:0;background:radial-gradient(circle at 25% 50%,#3a3f4a 0%,#1a2a40 40%,#0c1828 100%)" role="img" aria-label="Close-up of an eye over binary code"></div>
    <svg class="abs" style="left:119px;top:64px" width="22" height="22" viewBox="0 0 22 22">
      <circle cx="11" cy="11" r="9" fill="none" stroke="var(--orange)" stroke-width="1.5"/>
    </svg>
    <p class="abs head" style="left:0;width:261px;top:101px;font-size:8px;text-align:center;text-transform:uppercase">Section title</p>
  </section>

  <!-- 15 Thank you -->
  <section class="slide slide--dark">
    <div class="photo" style="inset:0;background:linear-gradient(135deg,#2b3c52 0%,#1a2c44 45%,#0f1e33 100%)" role="img" aria-label="Padlocks over a dark digital background"></div>
    <p class="abs head" style="left:145px;top:62px;font-size:7px;text-transform:uppercase">Thank you</p>
    <div class="abs" style="left:145px;top:74px;display:grid;row-gap:4px">
      <p style="display:flex;align-items:center;gap:3px;font-size:3px;color:#fff"><span style="width:4px;height:4px;border-radius:50%;background:var(--orange)"></span>4410 Calle Norte Ste 210</p>
      <p style="display:flex;align-items:center;gap:3px;font-size:3px;color:#fff"><span style="width:4px;height:4px;border-radius:50%;background:var(--orange)"></span>support@tervalo.com</p>
      <p style="display:flex;align-items:center;gap:3px;font-size:3px;color:#fff"><span style="width:4px;height:4px;border-radius:50%;background:var(--orange)"></span>www.tervalo.com</p>
    </div>
    <p class="abs brand" style="left:22px;top:118px;font-size:10px">Tervalo</p>
  </section>

</main>
</body>
</html>
```